Professional Photography Business cards

I need business cards that include my logo which I have uploaded. I run a photography business. I am open to ideas but I would like one side to have my logo and the other side to have my contact info. I don't have a website made but I do own a website domain. I have uploaded 2 different logo color schemes. My business colors are Blue, black , and white.

Business Name
Business Phone Number
Business Email
Business Website address
Instagram

Industry/Entity Type

Professional Photography

Contact Information for Business Card

Phone Number: 555-314-8027 email: info@tkellan-studios.example Instagram: @t.kellanstudios website doman- www.tkellan-studios.example

Requirements
Must have
• I like the idea of a business card with a full black background front and back of card. My colors must include royal blue, black, and white

```html
<!DOCTYPE html>
<html lang="en">
<head>
<meta charset="utf-8">
<title>T. Kellan Studios – Business Cards</title>
<link rel="stylesheet" href="https://fonts.googleapis.com/css2?family=Arimo:wght@400;700&display=swap">
<style>
  :root {
    --backdrop: #3a3a3c;
    --card: #1c1c1d;
    --royal-blue: #2b36a3;
    --white: #ffffff;
    --emboss: #2a2a2b;
    --emboss-ring: #4a4a4c;
  }
  * { margin: 0; padding: 0; box-sizing: border-box; }
  html, body { width: 1200px; height: 1059px; overflow: hidden; }
  body {
    background: var(--backdrop);
    font-family: "Arimo", Arial, sans-serif;
    position: relative;
  }
  .card {
    position: absolute;
    background: var(--card);
    border-radius: 20px;
    box-shadow: 0 10px 24px rgba(0,0,0,0.45);
  }
  .card--front { left: 257px; top: 100px; width: 687px; height: 391px; }
  .card--back  { left: 253px; top: 537px; width: 694px; height: 394px; }

  .brand {
    position: absolute;
    display: flex;
    align-items: center;
    gap: 14px;
    white-space: nowrap;
  }
  .brand__mark { border-radius: 50%; flex: none; }
  .brand__name { font-weight: 700; letter-spacing: 0.5px; }

  .card--front .brand { left: 160px; top: 160px; }
  .card--front .brand__mark { width: 52px; height: 52px; border: 5px solid var(--emboss-ring); }
  .card--front .brand__name { font-size: 40px; color: var(--emboss); }

  .card--back .brand { left: 52px; top: 176px; }
  .card--back .brand__mark { width: 34px; height: 34px; border: 4px solid var(--white); }
  .card--back .brand__name { font-size: 27px; color: var(--royal-blue); }

  .divider {
    position: absolute;
    left: 346px; top: 127px;
    width: 1px; height: 139px;
    background: var(--royal-blue);
  }
  .contact { position: absolute; left: 376px; top: 124px; color: var(--white); }
  .contact__name { font-size: 26px; font-weight: 700; color: var(--royal-blue); line-height: 1; }
  .contact__role { font-size: 15px; margin-top: 3px; }
  .contact__list { list-style: none; margin-top: 17px; }
  .contact__item {
    display: flex; align-items: center; gap: 9px;
    font-size: 16px; line-height: 21.5px;
  }
  .contact__icon { width: 11px; height: 11px; flex: none; fill: var(--royal-blue); }
  .contact__dot {
    width: 10px; height: 10px; flex: none;
    border-radius: 50%; background: var(--royal-blue);
  }
</style>
</head>
<body>
  <section class="card card--front">
    <div class="brand">
      <span class="brand__mark"></span>
      <span class="brand__name">T. Kellan Studios</span>
    </div>
  </section>

  <section class="card card--back">
    <div class="brand">
      <span class="brand__mark"></span>
      <span class="brand__name">T. Kellan Studios</span>
    </div>
    <div class="divider"></div>
    <div class="contact">
      <p class="contact__name">Dana Whitlow</p>
      <p class="contact__role">Managing Director</p>
      <ul class="contact__list">
        <li class="contact__item">
          <svg class="contact__icon" viewBox="0 0 24 24" aria-hidden="true"><path d="M6.6 10.8a15.2 15.2 0 0 0 6.6 6.6l2.2-2.2c.3-.3.7-.4 1-.2 1.1.4 2.3.6 3.6.6.6 0 1 .4 1 1V20c0 .6-.4 1-1 1A17 17 0 0 1 3 4c0-.6.4-1 1-1h3.5c.6 0 1 .4 1 1 0 1.3.2 2.5.6 3.6.1.3 0 .7-.2 1z"/></svg>
          555-314-8027
        </li>
        <li class="contact__item">
          <svg class="contact__icon" viewBox="0 0 24 24" aria-hidden="true"><path d="M2 5h20v14H2z M2 5l10 8 10-8" fill="none" stroke="var(--royal-blue)" stroke-width="2.5"/></svg>
          info@tkellan-studios.example
        </li>
        <li class="contact__item">
          <svg class="contact__icon" viewBox="0 0 24 24" aria-hidden="true"><circle cx="12" cy="12" r="10" fill="none" stroke="var(--royal-blue)" stroke-width="2.5"/><path d="M2 12h20M12 2c3 3 3 17 0 20M12 2c-3 3-3 17 0 20" fill="none" stroke="var(--royal-blue)" stroke-width="2"/></svg>
          www.tkellan-studios.example
        </li>
        <li class="contact__item">
          <span class="contact__dot"></span>
          @t.kellanstudios
        </li>
      </ul>
    </div>
  </section>
</body>
</html>
```